Brindle painting & waterproofing business card.

Business cards updated to reflect photos attached. we have given the photos of the old business cards and some of our updated designs for other items we have here in the office. Please see attached. if anyone needs to contact us directly for clarification you can email us at brindlerestoration@mailcove.example

Industry/Entity Type

Construction

Contact Information for Business Card

See attached photos

Font styles to use
Other font styles liked:
• Same as photos

Colors
ec1f27

Requirements
Must have
• Employee Names,
• Dennis Marlow II, Supervisor/Owner
• Dee Marlow, President/Owner
• Gus Tremby, Sales Representative
• Lyle Varsen, Supervisor
• Change 20 years to 25
Nice to have
• ideas reflecting the attached photos
Should not have
• should not be exactly like attached photos as those are old business card but reflect to match new logo listed as korvel van and cup photo.

```html
<!DOCTYPE html>
<html lang="en">
<head>
<meta charset="utf-8">
<title>Brindle's Painting &amp; Restoration – Business Cards</title>
<link rel="stylesheet" href="https://fonts.googleapis.com/css2?family=Roboto+Condensed:wght@300;400;700;900&display=swap">
<style>
  :root {
    --red: #ec1f27;
    --red-deep: #c8161d;
    --red-light: #f2444a;
    --card-white: #f4f4f4;
    --card-grey: #d9d9d9;
    --ink: #1e1e1e;
    --ink-soft: #555;
    --stage: #ecebe8;
  }
  * { box-sizing: border-box; margin: 0; padding: 0; }
  html, body { width: 1200px; height: 780px; overflow: hidden; }
  body {
    background: var(--stage);
    font-family: "Roboto Condensed", "Arial Narrow", sans-serif;
  }
  .card-sheet {
    width: 1200px;
    height: 780px;
    padding: 150px 30px;
    display: flex;
    flex-wrap: wrap;
    justify-content: center;
    align-content: center;
    gap: 40px 30px;
  }
  .card {
    position: relative;
    width: 360px;
    height: 206px;
    overflow: hidden;
    box-shadow: 0 5px 14px rgba(0,0,0,.18);
  }
  .card-front { background: linear-gradient(160deg, #fff 0%, var(--card-white) 45%, var(--card-grey) 100%); }
  .card-back { background: radial-gradient(circle at 55% 45%, var(--red-light) 0%, var(--red) 55%, var(--red-deep) 100%); }

  .front-swoosh { position: absolute; inset: 0; width: 100%; height: 100%; }

  .front-content { position: absolute; left: 22px; top: 18px; right: 20px; }
  .brand-name {
    font-weight: 900;
    text-transform: uppercase;
    line-height: .95;
    color: var(--red);
  }
  .card-front .brand-name { font-size: 24px; letter-spacing: .4px; }
  .card-front .brand-name .brand-sub { display: block; font-size: 17px; }

  .person-name {
    margin-top: 8px;
    font-size: 16px;
    font-weight: 400;
    color: var(--red);
    text-transform: uppercase;
    letter-spacing: .2px;
    line-height: 1.2;
  }
  .person-title {
    font-size: 10px;
    font-weight: 300;
    color: var(--ink-soft);
    text-transform: uppercase;
    letter-spacing: .5px;
  }
  .credentials {
    margin-top: 6px;
    font-size: 10px;
    color: var(--ink);
    text-transform: uppercase;
    line-height: 1.25;
  }
  .credentials strong { font-weight: 700; }
  .credentials .license { font-weight: 300; color: var(--ink-soft); }
  .contact-line {
    margin-top: 6px;
    font-size: 9px;
    color: var(--ink);
    line-height: 1.35;
  }
  .contact-line .label { color: var(--red); font-weight: 700; }

  .back-content {
    position: absolute; inset: 0;
    display: flex; flex-direction: column; align-items: center; justify-content: center;
    text-align: center;
  }
  .card-back .brand-name { color: #fff; font-size: 36px; }
  .card-back .brand-name .brand-sub { display: block; font-size: 25px; }
  .website {
    margin-top: 16px;
    color: #fde0e1;
    font-size: 10px;
    letter-spacing: 2.4px;
    text-transform: uppercase;
  }
</style>
</head>
<body>
<main class="card-sheet">

  <section class="card card-back" aria-label="Business card back">
    <div class="back-content">
      <h2 class="brand-name">Brindle's<span class="brand-sub">Painting &amp; Restoration</span></h2>
      <p class="website">www.brindlerestoration.example</p>
    </div>
  </section>

  <section class="card card-front" aria-label="Business card front, Dennis Marlow II">
    <svg class="front-swoosh" viewBox="0 0 360 206" preserveAspectRatio="none" aria-hidden="true">
      <path d="M200 206 C 270 188, 330 140, 360 70 L360 206 Z" fill="#ec1f27"/>
      <path d="M200 206 C 270 188, 330 140, 360 70" fill="none" stroke="#bdbdbd" stroke-width="2.5"/>
    </svg>
    <div class="front-content">
      <h1 class="brand-name">Brindle's<span class="brand-sub">Painting &amp; Restoration</span></h1>
      <p class="person-name">Dennis Marlow II</p>
      <p class="person-title">Supervisor/Owner</p>
      <p class="credentials"><strong>General Contractor</strong> <span class="license">CGC#4830261</span><br><strong>Licensed &amp; Insured</strong></p>
      <p class="contact-line">
        <span class="label">O:</span> 555.214.3608 | <span class="label">M:</span> 555.214.7719<br>
        <span class="label">E:</span> brindlerestoration@mailcove.example<br>
        2140 Harlow Ave, Seabrook Bch, FL 30999
      </p>
    </div>
  </section>

  <section class="card card-front" aria-label="Business card front, Dee Marlow">
    <svg class="front-swoosh" viewBox="0 0 360 206" preserveAspectRatio="none" aria-hidden="true">
      <path d="M200 206 C 270 188, 330 140, 360 70 L360 206 Z" fill="#ec1f27"/>
      <path d="M200 206 C 270 188, 330 140, 360 70" fill="none" stroke="#bdbdbd" stroke-width="2.5"/>
    </svg>
    <div class="front-content">
      <h2 class="brand-name">Brindle's<span class="brand-sub">Painting &amp; Restoration</span></h2>
      <p class="person-name">Dee Marlow</p>
      <p class="person-title">President/Owner</p>
      <p class="credentials"><strong>General Contractor</strong> <span class="license">CGC#4830261</span><br><strong>Licensed &amp; Insured</strong></p>
      <p class="contact-line">
        <span class="label">O:</span> 555.214.3608 | <span class="label">M:</span> 555.214.8842<br>
        <span class="label">E:</span> brindlerestoration@mailcove.example<br>
        2140 Harlow Ave, Seabrook Bch, FL 30999
      </p>
    </div>
  </section>

  <section class="card card-front" aria-label="Business card front, Gus Tremby">
    <svg class="front-swoosh" viewBox="0 0 360 206" preserveAspectRatio="none" aria-hidden="true">
      <path d="M200 206 C 270 188, 330 140, 360 70 L360 206 Z" fill="#ec1f27"/>
      <path d="M200 206 C 270 188, 330 140, 360 70" fill="none" stroke="#bdbdbd" stroke-width="2.5"/>
    </svg>
    <div class="front-content">
      <h2 class="brand-name">Brindle's<span class="brand-sub">Painting &amp; Restoration</span></h2>
      <p class="person-name">Gus Tremby</p>
      <p class="person-title">Sales Representative</p>
      <p class="credentials"><strong>General Contractor</strong> <span class="license">CGC#4830261</span><br><strong>Licensed &amp; Insured</strong></p>
      <p class="contact-line">
        <span class="label">O:</span> 555.214.3608 | <span class="label">M:</span> 555.214.5170<br>
        <span class="label">E:</span> brindlerestoration@mailcove.example<br>
        2140 Harlow Ave, Seabrook Bch, FL 30999
      </p>
    </div>
  </section>

  <section class="card card-front" aria-label="Business card front, Lyle Varsen">
    <svg class="front-swoosh" viewBox="0 0 360 206" preserveAspectRatio="none" aria-hidden="true">
      <path d="M200 206 C 270 188, 330 140, 360 70 L360 206 Z" fill="#ec1f27"/>
      <path d="M200 206 C 270 188, 330 140, 360 70" fill="none" stroke="#bdbdbd" stroke-width="2.5"/>
    </svg>
    <div class="front-content">
      <h2 class="brand-name">Brindle's<span class="brand-sub">Painting &amp; Restoration</span></h2>
      <p class="person-name">Lyle Varsen</p>
      <p class="person-title">Supervisor</p>
      <p class="credentials"><strong>General Contractor</strong> <span class="license">CGC#4830261</span><br><strong>Licensed &amp; Insured</strong></p>
      <p class="contact-line">
        <span class="label">O:</span> 555.214.3608 | <span class="label">M:</span> 555.214.6293<br>
        <span class="label">E:</span> brindlerestoration@mailcove.example<br>
        2140 Harlow Ave, Seabrook Bch, FL 30999
      </p>
    </div>
  </section>

</main>
</body>
</html>
```